Residential Construction Business - Site Signage

I need a design made for a site fence banner. We have a logo and branding so the design would need to be aligned with this. It would need to be made to specific size ratio so that it can be sent to the maker for production.
ratio : 4600 wide x 1700 high
The design should feature our website and also the slogan
"don't move, re-imagine"

Target Market(s)

potential clients

Industry/Entity Type

construction

Font styles to use
Other font styles liked:
• to match branding

Colors
0054AA
0677BA
7BADD7
CADEEF
E8F1F8

Requirements
Must have
• www.velmbuild.com.au Majority of the sign is our brand logo
Nice to have
• Majority of the sign is our brand logo
Should not have
• colors and themes that arent brand relevant

```html
<!DOCTYPE html>
<html lang="en">
<head>
<meta charset="utf-8">
<title>Velm Build – Site Fence Banner</title>
<link rel="stylesheet" href="https://fonts.googleapis.com/css2?family=Montserrat:wght@500;700&display=swap">
<style>
  :root {
    --stage: #e6e7e8;
    --banner-white: #f1f1f0;
    --brand-navy: #1d4a72;
    --slogan-navy: #1b3d62;
    --charcoal: #2a2d2f;
    --pattern-grey: #d9d9da;
  }
  * { margin: 0; padding: 0; box-sizing: border-box; }
  html, body {
    width: 1200px;
    height: 842px;
    overflow: hidden;
    background: var(--stage);
    font-family: "Montserrat", Arial, sans-serif;
  }
  .banner {
    position: absolute;
    left: 20px;
    top: 206px;
    width: 1160px;
    height: 429px;
    background: var(--banner-white);
    overflow: hidden;
  }
  .banner-shapes {
    position: absolute;
    inset: 0;
    width: 100%;
    height: 100%;
  }
  .brand-name {
    position: absolute;
    left: 306px;
    top: 192px;
    font-size: 30px;
    font-weight: 500;
    letter-spacing: 0.36em;
    line-height: 1;
    color: var(--charcoal);
    white-space: nowrap;
  }
  .slogan {
    position: absolute;
    left: 651px;
    top: 143px;
    height: 128px;
    padding-left: 18px;
    border-left: 5px solid var(--slogan-navy);
    font-size: 56px;
    font-weight: 700;
    line-height: 1.12;
    letter-spacing: 0.01em;
    white-space: nowrap;
  }
  .slogan-line-primary { display: block; color: var(--slogan-navy); margin-top: -4px; }
  .slogan-line-secondary { display: block; color: var(--charcoal); }
  .website {
    position: absolute;
    left: 651px;
    top: 362px;
    font-size: 20.5px;
    font-weight: 700;
    letter-spacing: 0.03em;
    color: var(--slogan-navy);
    text-transform: uppercase;
    white-space: nowrap;
  }
</style>
</head>
<body>
  <main class="banner">
    <svg class="banner-shapes" viewBox="0 0 1160 429" preserveAspectRatio="none" aria-hidden="true">
      <defs>
        <linearGradient id="pattern-fade" x1="0" y1="0" x2="1" y2="0">
          <stop offset="0" stop-color="#f1f1f0" stop-opacity="0"/>
          <stop offset="1" stop-color="#d6d6d7" stop-opacity="0.7"/>
        </linearGradient>
      </defs>
      <rect class="geometric-backdrop" x="620" y="0" width="540" height="429" fill="url(#pattern-fade)" role="img" aria-label="Faint grey geometric line pattern"/>
      <path class="brand-chevron" d="M0 0 H394 L288 200 Q283 210 288 220 L404 429 H0 Z" fill="var(--brand-navy)"/>
    </svg>

    <div class="brand-name">VELM BUILD</div>

    <h1 class="slogan">
      <span class="slogan-line-primary">DON’T MOVE,</span>
      <span class="slogan-line-secondary">RE-IMAGINE</span>
    </h1>

    <p class="website">www.velmbuild.com.au</p>
  </main>
</body>
</html>
```